Business Card Design needed for logo design project

Our company needs a Business Card Design. Please refer to our original project in the link above.

Industry/Entity Type

Business

```html
<!DOCTYPE html>
<html lang="en">
<head>
<meta charset="utf-8">
<title>Orven Business Card</title>
<link rel="stylesheet" href="https://fonts.googleapis.com/css2?family=Source+Sans+3:wght@400;600;700&display=swap">
<style>
  :root {
    --backdrop: #3a3a3a;
    --card: #f6f6f6;
    --brand-blue: #0e3f8a;
    --tab-navy: #0b2b5e;
    --accent-red: #d8262b;
    --ink: #444444;
    --icon: #1f4d8f;
  }
  * { margin: 0; padding: 0; box-sizing: border-box; }
  html, body {
    width: 1200px; height: 750px; overflow: hidden;
    background: var(--backdrop);
    font-family: "Source Sans 3", "Myriad Pro", Arial, sans-serif;
  }
  .stage { position: relative; width: 1200px; height: 750px; }
  .card {
    position: absolute; top: 218px;
    width: 492px; height: 281px;
    background: var(--card);
    overflow: hidden;
  }
  .card--front { left: 91px; }
  .card--back { left: 620px; }

  .front-tab {
    position: absolute; left: 0; top: 49px;
    width: 12px; height: 188px;
    background: var(--tab-navy);
    border-radius: 0 4px 4px 0;
  }
  .person-name {
    position: absolute; left: 42px; top: 48px;
    font-size: 19px; font-weight: 600; color: var(--brand-blue);
  }
  .person-role {
    position: absolute; left: 41px; top: 71px;
    font-size: 14px; color: var(--accent-red);
  }
  .address {
    position: absolute; left: 43px; top: 98px;
    font-size: 13px; line-height: 17px; color: var(--ink);
  }
  .contact-list {
    position: absolute; left: 42px; top: 144px;
    list-style: none;
  }
  .contact-list li {
    display: flex; align-items: center;
    height: 18.6px;
    font-size: 13px; color: var(--ink);
  }
  .contact-list svg {
    width: 13px; height: 13px; margin-right: 8px; flex: none;
    fill: var(--icon);
  }
  .brand {
    position: absolute; display: flex; align-items: center;
    font-weight: 700; color: var(--brand-blue); line-height: 1;
    white-space: nowrap;
  }
  .brand-dot { border-radius: 50%; background: var(--accent-red); flex: none; }
  .brand--front { left: 264px; top: 184px; font-size: 44px; letter-spacing: 1px; }
  .brand--front .brand-dot { width: 15px; height: 15px; margin-right: 10px; }
  .brand--back { left: 318px; top: 208px; font-size: 36px; letter-spacing: 0.5px; }
  .brand--back .brand-dot { width: 12px; height: 12px; margin-right: 8px; }
  .web-address {
    position: absolute; left: 330px; top: 247px;
    font-size: 13px; letter-spacing: 3px; color: var(--ink);
  }
</style>
</head>
<body>
<main class="stage">
  <section class="card card--front">
    <div class="front-tab"></div>
    <h1 class="person-name">John Smith</h1>
    <p class="person-role">Director</p>
    <p class="address">Suite 102 Street name<br>State, Zip 2034,Country</p>
    <ul class="contact-list">
      <li>
        <svg viewBox="0 0 16 16" aria-hidden="true"><path d="M1 5c0-2 3-3 7-3s7 1 7 3v1h-4V5H5v1H1zM3 7h10l1 7H2zm5 2a2 2 0 1 0 0 4 2 2 0 0 0 0-4z"/></svg>
        127 345 9876
      </li>
      <li>
        <svg viewBox="0 0 16 16" aria-hidden="true"><path d="M4 0h8a1 1 0 0 1 1 1v14a1 1 0 0 1-1 1H4a1 1 0 0 1-1-1V1a1 1 0 0 1 1-1zm1 2v10h6V2zm3 11a1 1 0 1 0 0 2 1 1 0 0 0 0-2z"/></svg>
        345 345 9876
      </li>
      <li>
        <svg viewBox="0 0 16 16" aria-hidden="true"><path d="M4 1h8v4H4zM1 6h14v6h-3v3H4v-3H1zm4 4v3h6v-3z"/></svg>
        345 345 9876
      </li>
      <li>
        <svg viewBox="0 0 16 16" aria-hidden="true"><path d="M1 3h14v10H1zm1.5 1.5L8 9l5.5-4.5v7h-11z"/></svg>
        info@yourname.com
      </li>
      <li>
        <svg viewBox="0 0 16 16" aria-hidden="true"><path d="M8 1a7 7 0 1 0 0 14A7 7 0 0 0 8 1zm0 1.3c.8.6 1.5 2 1.8 3.7H6.2C6.5 4.3 7.2 2.9 8 2.3zM2.4 7h2.8v2H2.4a5.6 5.6 0 0 1 0-2zm3.8 0h3.6v2H6.2zm4.6 0h2.8a5.6 5.6 0 0 1 0 2h-2.8zM6.2 10h3.6c-.3 1.7-1 3.1-1.8 3.7-.8-.6-1.5-2-1.8-3.7z"/></svg>
        www.yourweb.com
      </li>
    </ul>
    <div class="brand brand--front"><span class="brand-dot"></span>ORVEN</div>
  </section>

  <section class="card card--back">
    <div class="brand brand--back"><span class="brand-dot"></span>ORVEN</div>
    <p class="web-address">www.orven.com</p>
  </section>
</main>
</body>
</html>
```